Wordpress Design Project

We are a Computer / Information Technology Company that will focus on the after-hours technical support for Home and Businesses.

I'm looking to have the home page as a static page with a links to blog, about us.

www.rkwidget.com.au is my web site.

Please do not chage uploaded logo's, do not copy current logo on website use uploaded files only, thanks.
Updates

Project Deadline Extended
Reason: No idea how this was posted with only 2 days!!

Cheers

Marcus

Project Deadline Extended
Reason: I have asked for some changes from designers.

Target Market(s)

Home and Small office/home office, or SOHO Computer users.

Industry/Entity Type

Computer

Requirements
Should not have
• After hours tech support added to logo.

```html
<!DOCTYPE html>
<html lang="en">
<head>
<meta charset="utf-8">
<title>RK Widget – After Hours Tech Support</title>
<link href="https://fonts.googleapis.com/css2?family=Montserrat:wght@600;700&family=Arimo:wght@400;700&display=swap" rel="stylesheet">
<style>
  :root {
    --brand-blue: #1a56a5;
    --link-blue: #1f5fae;
    --text-dark: #333333;
    --text-grey: #666666;
    --panel-grey: #ebebeb;
    --footer-grey: #e6e6e6;
    --nav-dark: #333333;
    --nav-active: #1d5ea8;
    --hero-deep: #0d3f86;
    --hero-mid: #1a5fb0;
    --row-grey: #7b7b7b;
    --rule: #c9c9c9;
    --accent-red: #a11818;
  }
  * { box-sizing: border-box; margin: 0; padding: 0; }
  html, body { width: 1020px; height: 1200px; overflow: hidden; background: #ffffff; }
  body { font-family: "Arimo", Arial, sans-serif; color: var(--text-dark); }
  .page { position: relative; width: 1000px; height: 1200px; }

  /* header */
  .site-header { position: absolute; left: 0; top: 0; width: 1000px; height: 84px; background: #fff; }
  .brand { position: absolute; left: 20px; top: 16px; display: flex; align-items: center; gap: 14px; }
  .brand-dot { width: 46px; height: 46px; border-radius: 50%; background: var(--brand-blue); }
  .brand-name { font-family: "Montserrat", sans-serif; font-weight: 600; font-size: 44px; color: var(--brand-blue); line-height: 50px; }
  .quick-contact { position: absolute; right: 20px; top: 18px; text-align: right; }
  .quick-contact .label { font-size: 16px; color: #222; }
  .quick-contact .phone { font-size: 20px; font-weight: 700; color: var(--brand-blue); margin-top: 2px; }

  /* hero */
  .hero { position: absolute; left: 0; top: 84px; width: 1000px; height: 316px;
    background: radial-gradient(circle at 75% 40%, var(--hero-mid), var(--hero-deep) 75%); overflow: hidden; }
  .hero-photo { position: absolute; left: 24px; top: 30px; width: 440px; height: 286px;
    background: linear-gradient(160deg, #c9ced6 0%, #8f97a3 55%, #2b2f36 100%); border-radius: 4px 4px 0 0; }
  .hero-band { position: absolute; left: 470px; top: 90px; width: 530px; height: 142px; background: rgba(60,130,210,.35); }
  .hero-title { position: absolute; left: 498px; top: 121px; font-size: 15px; font-weight: 700; color: #d6dbe3; }
  .hero-copy { position: absolute; left: 498px; top: 146px; width: 460px; font-size: 15px; line-height: 26px; color: #fff; }
  .hero-arrow { position: absolute; top: 160px; width: 32px; height: 32px; }
  .hero-arrow.prev { left: 21px; } .hero-arrow.next { left: 947px; }

  /* nav row */
  .nav-row { position: absolute; left: 0; top: 400px; width: 1000px; height: 46px; background: var(--panel-grey); }
  .nav-bar { position: absolute; left: 0; top: 0; }
  .search-label { position: absolute; left: 33px; top: 24px; font-size: 12px; color: #444; }
  .search-input { position: absolute; left: 80px; top: 14px; width: 246px; height: 33px; background: #d7d7d7;
    border: 1px solid #b5b5b5; font-size: 12px; color: #999; padding: 9px 12px; }
  .search-icon { position: absolute; left: 331px; top: 20px; }
  .nav-item { position: absolute; top: 0; height: 46px; line-height: 48px; color: #fff; font-size: 15px; text-align: center; }
  .nav-item.active { background: var(--nav-active); }

  /* welcome panel */
  .welcome-panel { position: absolute; left: 0; top: 446px; width: 1000px; height: 326px; background: var(--panel-grey); }
  .section-title { position: absolute; font-family: "Montserrat", sans-serif; font-weight: 700; font-size: 20px; color: var(--brand-blue); line-height: 26px; }
  .intro { position: absolute; left: 34px; top: 82px; width: 596px; font-size: 12px; line-height: 18px; color: var(--text-dark); }
  .service-list { position: absolute; list-style: none; font-size: 12px; line-height: 25px; color: var(--link-blue); }
  .service-list li { position: relative; padding-left: 17px; }
  .service-list li::before { content: ""; position: absolute; left: 0; top: 10px; width: 6px; height: 6px; background: var(--brand-blue); }
  .v-rule { position: absolute; width: 1px; background: var(--rule); }
  .post { position: absolute; left: 692px; width: 290px; height: 92px; }
  .thumb { position: absolute; left: 0; top: 0; width: 90px; height: 92px; background: linear-gradient(135deg, #3b3f47, #0f1216 60%, #2a5fb0); }
  .post-title { position: absolute; left: 104px; top: 12px; font-size: 12px; font-weight: 700; color: #222; }
  .post-text { position: absolute; left: 104px; top: 32px; width: 176px; font-size: 12px; line-height: 18px; color: var(--text-grey); }
  .h-rule { position: absolute; height: 1px; background: var(--rule); }
  .more-post { position: absolute; left: 921px; top: 297px; font-size: 12px; color: var(--accent-red); }

  /* lower columns */
  .entry { position: absolute; width: 300px; height: 66px; }
  .avatar { position: absolute; left: 0; top: 0; width: 64px; height: 64px; background: linear-gradient(160deg, #b89a7f, #7d6a5a); border: 1px solid #ccc; }
  .entry-name { position: absolute; left: 74px; top: 2px; font-size: 12px; font-weight: 700; color: #111; }
  .entry-meta { position: absolute; left: 74px; top: 2px; font-size: 12px; color: #999; }
  .entry-text { position: absolute; left: 74px; top: 21px; width: 230px; font-size: 12px; line-height: 18px; color: var(--text-dark); }
  .entry-text a { color: var(--accent-red); text-decoration: none; }
  .hours { position: absolute; left: 681px; top: 850px; width: 299px; }
  .hours-row { position: relative; height: 26px; margin-bottom: 4px; background: var(--row-grey); color: #fff; font-size: 12px; line-height: 26px; }
  .hours-row span { position: absolute; top: 0; }
  .hours-row .day { left: 52px; } .hours-row .sep { left: 110px; } .hours-row .time { left: 146px; }

  /* footer */
  .site-footer { position: absolute; left: 0; top: 1097px; width: 1000px; height: 103px; background: var(--footer-grey); }
  .footer-links { position: absolute; left: 0; width: 1000px; top: 15px; text-align: center; font-size: 12px; color: #333; }
  .copyright { position: absolute; left: 0; width: 1000px; top: 42px; text-align: center; font-size: 12px; color: #333; }
  .follow { position: absolute; left: 915px; top: 15px; font-size: 12px; color: #333; }
  .social { position: absolute; left: 828px; top: 36px; display: flex; gap: 10px; }
  .social span { width: 20px; height: 20px; background: #333; border-radius: 3px; }
</style>
</head>
<body>
<div class="page">

  <header class="site-header">
    <div class="brand"><span class="brand-dot"></span><span class="brand-name">RK Widget</span></div>
    <div class="quick-contact">
      <div class="label">Quick contact:</div>
      <div class="phone">020 5550 4716</div>
    </div>
  </header>

  <section class="hero">
    <div class="hero-photo" role="img" aria-label="Desktop computer with monitor, tower and keyboard"></div>
    <div class="hero-band"></div>
    <div class="hero-title">Lorem Ipsum is simply dummy text of the printing</div>
    <div class="hero-copy">It was popularised in the 1960s with the release of transfer sheets containing Lorem Ipsum passages, and more recently</div>
    <svg class="hero-arrow prev" viewBox="0 0 32 32" aria-label="Previous slide"><circle cx="16" cy="16" r="16" fill="#d7e4f3"/><path d="M23 16H10M15 10l-6 6 6 6" fill="none" stroke="#1d5ea8" stroke-width="3" stroke-linecap="round" stroke-linejoin="round"/></svg>
    <svg class="hero-arrow next" viewBox="0 0 32 32" aria-label="Next slide"><circle cx="16" cy="16" r="16" fill="#d7e4f3"/><path d="M9 16h13M17 10l6 6-6 6" fill="none" stroke="#1d5ea8" stroke-width="3" stroke-linecap="round" stroke-linejoin="round"/></svg>
  </section>

  <div class="nav-row">
    <svg class="nav-bar" width="1000" height="46" viewBox="0 0 1000 46"><path d="M360 0H1000V46H410C404 20 392 4 360 0Z" fill="#333333"/></svg>
    <span class="search-label">Search</span>
    <div class="search-input">Type your keay word here</div>
    <svg class="search-icon" width="24" height="24" viewBox="0 0 24 24" aria-label="Search"><circle cx="10" cy="10" r="7" fill="#dfe9f5" stroke="#555" stroke-width="2"/><path d="M15 15l6 6" stroke="#333" stroke-width="3" stroke-linecap="round"/></svg>
    <a class="nav-item active" style="left:436px;width:76px">Home</a>
    <a class="nav-item" style="left:560px;width:100px">About Us</a>
    <a class="nav-item" style="left:703px;width:80px">Blog</a>
    <a class="nav-item" style="left:828px;width:110px">Contact Us</a>
  </div>

  <section class="welcome-panel">
    <h1 class="section-title" style="left:31px;top:39px">Welcome To Our Company</h1>
    <p class="intro">Contrary to popular belief, Lorem Ipsum is not simply random text. It has roots in a piece of classical Latin literature from 45 BC, making it over 2000 years old. A Latin professor at a small college in the hills looked up one of the more obscure Latin words, consectetur, from a Lorem Ipsum passage, and going through the cites of the word in classical literature, discovered the undoubtable source. Lorem Ipsum comes from sections 1.10.32 and 1.10.33 of an old text on the ends of good and evil, written by an old author in 45 BC. This book is a treatise on ethics, very popular during the Renaissance.</p>
    <ul class="service-list" style="left:36px;top:214px">
      <li>No job is too small for any PC:</li><li>Home ADSL.</li><li>Wireless.</li>
    </ul>
    <ul class="service-list" style="left:247px;top:214px;width:160px">
      <li>Virus removal.</li><li>System configuration and installation.</li>
    </ul>
    <ul class="service-list" style="left:436px;top:214px">
      <li>Laptop configuration and installation.</li><li>Hardware.</li>
    </ul>
    <div class="v-rule" style="left:663px;top:36px;height:258px"></div>
    <h2 class="section-title" style="left:691px;top:35px">Recent Post</h2>
    <article class="post" style="top:76px">
      <div class="thumb" role="img" aria-label="Desktop computer tower and monitor"></div>
      <div class="post-title">Lorem Ipsum is simply dummy</div>
      <div class="post-text">It was popularised in the 1960s with the release of transfer sheets containing.</div>
    </article>
    <div class="h-rule" style="left:740px;top:182px;width:193px"></div>
    <article class="post" style="top:196px">
      <div class="thumb" role="img" aria-label="Desktop computer tower and monitor"></div>
      <div class="post-title">Lorem Ipsum is simply dummy</div>
      <div class="post-text">It was popularised in the 1960s with the release of transfer sheets containing.</div>
    </article>
    <a class="more-post">more post</a>
  </section>

  <h2 class="section-title" style="left:23px;top:793px">Recent Comments</h2>
  <h2 class="section-title" style="left:350px;top:793px">Archives</h2>
  <h2 class="section-title" style="left:691px;top:791px;width:290px">After Hours Appointments Available</h2>
  <div class="v-rule" style="left:338px;top:812px;height:258px"></div>
  <div class="v-rule" style="left:663px;top:812px;height:258px"></div>

  <div class="entry" style="left:26px;top:836px"><div class="avatar" role="img" aria-label="Commenter portrait"></div><div class="entry-name">Owen</div><div class="entry-text">Contrary to popular belief, Lorem Ipsum is not simply random text.</div></div>
  <div class="h-rule" style="left:36px;top:914px;width:262px"></div>
  <div class="entry" style="left:26px;top:927px"><div class="avatar" role="img" aria-label="Commenter portrait"></div><div class="entry-name">Owen</div><div class="entry-text">Contrary to popular belief, Lorem Ipsum is not simply random text.</div></div>
  <div class="h-rule" style="left:36px;top:1004px;width:262px"></div>
  <div class="entry" style="left:26px;top:1017px"><div class="avatar" role="img" aria-label="Commenter portrait"></div><div class="entry-name">Owen</div><div class="entry-text">Contrary to popular belief, Lorem Ipsum is not simply random text.</div></div>

  <div class="entry" style="left:352px;top:836px"><div class="avatar" role="img" aria-label="Author portrait"></div><div class="entry-meta">1 day ago</div><div class="entry-text">Contrary to popular belief, Lorem Ipsum is not simply random text. <a>read more</a></div></div>
  <div class="h-rule" style="left:362px;top:914px;width:262px"></div>
  <div class="entry" style="left:352px;top:927px"><div class="avatar" role="img" aria-label="Author portrait"></div><div class="entry-meta">1 day ago</div><div class="entry-text">Contrary to popular belief, Lorem Ipsum is not simply random text.&nbsp; <a>read more</a></div></div>
  <div class="h-rule" style="left:362px;top:1004px;width:262px"></div>
  <div class="entry" style="left:352px;top:1017px"><div class="avatar" role="img" aria-label="Author portrait"></div><div class="entry-meta">1 day ago</div><div class="entry-text">Contrary to popular belief, Lorem Ipsum is not simply random text.&nbsp; <a>read more</a></div></div>

  <div class="hours">
    <div class="hours-row"><span class="day">Mon</span><span class="sep">:</span><span class="time">6:00 PM-9:00 PM</span></div>
    <div class="hours-row"><span class="day">Tue</span><span class="sep">:</span><span class="time">6:00 PM-9:00 PM</span></div>
    <div class="hours-row"><span class="day">Wed</span><span class="sep">:</span><span class="time">6:00 PM-9:00 PM</span></div>
    <div class="hours-row"><span class="day">Thu</span><span class="sep">:</span><span class="time">6:00 PM-9:00 PM</span></div>
    <div class="hours-row"><span class="day">Fri</span><span class="sep">:</span><span class="time">6:00 PM-9:00 PM</span></div>
    <div class="hours-row"><span class="day">Sat</span><span class="sep">:</span><span class="time">10:00 AM-9:00 PM</span></div>
    <div class="hours-row"><span class="day">Sun</span><span class="sep">:</span><span class="time">10:00 AM-9:00 PM</span></div>
  </div>

  <footer class="site-footer">
    <div class="footer-links">Home | About Us | Blog | Contact Us</div>
    <div class="copyright">2011 ©&nbsp; all copyrights.rkwidget.received</div>
    <div class="follow">follow us</div>
    <div class="social"><span></span><span></span><span></span><span></span><span></span></div>
  </footer>

</div>
</body>
</html>
```